Wordpress Design Project for CLG

We need a clean word press design for a new event planning company called Marigold Gathering & Occasions. We assist planners or leaders who are in charge of planning conferences, meetings, or conventions. In addition, we offer small business development strategy. We do not decorate: we help clients negotiate better contracts and/ or develop better systems to become more efficient. I want people to come to this site for referrals for other businesses and for training information.
I would like to see a design that uses the colors in the logo. The final design should be creative, professional, and innovative.
Industry/Entity Type
Event Planning
Requirements
Must have
- user friendly! easy to Navigate!
I like the feel of the following websites:
http://www.ventureowls.com.au/
http://galatrove.com/
Obviously, I will need to grow to that size of a site but I love it...
1.Client Sign in portal-
2. Social media and blog friendly!! I want people to use the site on a regular. I will post video, articles, and social media daily.
visitors can sign up or in using social media
very open to suggestions
Landing page for site that allows visitor to decide what they want to visit (button)- should be catchy
a. Convention & Meeting Services
b. Social Events
c. Small Business Solutions
2. Tabs
a. Home (ability to have pic gallery rotating)
b. About CLG
c. Contact us
d. Convention & Meeting services
e. Social Events
f. Small Business Solutions
g. Testimonials
Nice to have
- Mobile friendly, very clean design

```html
<!DOCTYPE html>
<html lang="en">
<head>
<meta charset="utf-8">
<title>Marigold Gathering &amp; Occasions</title>
<link href="https://fonts.googleapis.com/css2?family=Questrial&display=swap" rel="stylesheet">
<style>
:root{
  --page:#ffffff;
  --header:#f1f1f1;
  --nav:#8c7fd3;
  --nav-light:#cfc8f0;
  --nav-active:#4f3fa8;
  --heading:#3b2f7d;
  --text:#222222;
  --muted:#7a7a7a;
  --button:#e2372a;
  --footer:#3e3e3e;
  --brand:#8d4aa5;
}
*{margin:0;padding:0;box-sizing:border-box}
html,body{width:903px;height:1200px;overflow:hidden}
body{position:relative;background:var(--page);font-family:"Questrial",sans-serif;color:var(--text)}
.abs{position:absolute}
.site-header{left:0;top:0;width:903px;height:141px;background:var(--header)}
.brand{left:110px;top:80px;display:flex;align-items:center;gap:8px;font-size:17px;color:var(--brand)}
.brand-dot{width:12px;height:12px;border-radius:50%;background:var(--brand)}
.search{left:640px;top:103px;width:164px;height:18px;border:1px solid #d8d8d8;border-radius:9px;background:#fff;font-size:8px;color:#999;padding:4px 10px}
.search svg{position:absolute;right:7px;top:4px}
.main-nav{left:0;top:141px;width:903px;height:45px;background:var(--nav)}
.nav-strip{left:0;top:186px;width:903px;height:5px;background:var(--nav-light)}
.nav-active{left:110px;top:186px;width:75px;height:5px;background:var(--nav-active)}
.main-nav ul{list-style:none;display:flex;gap:26px;position:absolute;left:117px;top:13px;color:#fff;font-size:15px}
.hero{left:91px;top:203px;width:723px;height:246px;background:linear-gradient(180deg,#3a1c3c 0%,#7e2a3e 35%,#c0415a 65%,#3a1522 100%)}
.hero-brand{left:172px;top:293px;width:167px;height:72px;background:#fff;display:flex;align-items:center;justify-content:center;gap:6px;font-size:11px;color:#777}
.hero-brand span.sq{width:9px;height:9px;background:#999}
.arrow{width:32px;height:32px}
h2{position:absolute;font-weight:400;font-size:19px;color:var(--heading)}
.photo{position:absolute}
.about-text{left:317px;top:522px;width:248px;font-size:8.6px;line-height:15.2px;color:var(--muted);text-align:justify}
.item-title{position:absolute;font-size:11.5px;line-height:15px;width:138px;text-align:justify;text-align-last:justify}
.item-title.short{text-align-last:left}
.item-desc{position:absolute;font-size:8.4px;line-height:13.5px;width:138px;color:#444;text-align:justify}
.btn{position:absolute;background:var(--button);color:#fff;font-size:9.5px;display:flex;align-items:center;justify-content:center;height:22px}
.site-footer{left:0;top:1126px;width:903px;height:74px;background:var(--footer);color:#fff}
.footer-links{position:absolute;left:0;width:903px;top:26px;text-align:center;font-size:9px;word-spacing:1px}
.footer-links span{margin:0 10px}
.copyright{position:absolute;left:0;width:903px;top:53px;text-align:center;font-size:8.5px;color:#ddd}
</style>
</head>
<body>
<header class="site-header abs">
  <div class="brand abs"><span class="brand-dot"></span>Marigold Gathering &amp; Occasions</div>
  <div class="search abs">Search
    <svg width="9" height="9" viewBox="0 0 10 10"><circle cx="4" cy="4" r="3" fill="none" stroke="#888" stroke-width="1.2"/><line x1="6" y1="6" x2="9" y2="9" stroke="#888" stroke-width="1.4"/></svg>
  </div>
</header>
<nav class="main-nav abs">
  <ul><li>About Us</li><li>Convention &amp; Meeting Services</li><li>Social Events</li><li>Small Business</li><li>Testimonial</li></ul>
</nav>
<div class="nav-strip abs"></div>
<div class="nav-active abs"></div>

<section class="hero abs" role="img" aria-label="Ballroom lit in red and pink with a blue patterned ceiling drum"></section>
<div class="hero-brand abs"><span class="sq"></span>Marigold Gathering &amp; Occasions</div>
<svg class="arrow abs" style="left:117px;top:403px" viewBox="0 0 32 32"><circle cx="16" cy="16" r="15" fill="#fff" stroke="#222" stroke-width="1.5"/><path d="M23 16H10M15 10l-6 6 6 6" fill="none" stroke="#d22" stroke-width="3"/></svg>
<svg class="arrow abs" style="left:755px;top:403px" viewBox="0 0 32 32"><circle cx="16" cy="16" r="15" fill="#fff" stroke="#222" stroke-width="1.5"/><path d="M9 16h13M17 10l6 6-6 6" fill="none" stroke="#222" stroke-width="3"/></svg>

<h2 style="left:100px;top:482px">About Us</h2>
<div class="photo" style="left:100px;top:525px;width:208px;height:126px;background:radial-gradient(circle at 30% 30%,#f6c04a,#c26a1a 40%,#2a150a 85%)" role="img" aria-label="Concert crowd with raised hands under stage lights"></div>
<p class="about-text abs">At vero eos et accusamus et iusto odio dignissimos ducimus qui blanditiis praesentium voluptatum deleniti atque corrupti quos dolores et quas molestias excepturi sint occaecati cupiditate non provident, similique sunt in culpa qui officia deserunt mollitia animi, id est laborum et dolorum fuga. Et harum quidem rerum facilis est et expedita distinctio. Nam libero tempore, cum soluta nobis est eligendi optio cumque nihil impedit quo minus id quod maxime placeat facere possimus.</p>

<h2 style="left:580px;top:482px">Featured Videos</h2>
<div class="photo" style="left:578px;top:525px;width:227px;height:126px;background:linear-gradient(180deg,#6a3410,#c57a2a 45%,#2a1508)" role="img" aria-label="Video still of a banquet hall set with round tables"></div>
<svg class="abs" style="left:578px;top:525px" width="227" height="126" viewBox="0 0 227 126">
  <rect x="130" y="55" width="16" height="12" rx="2" fill="#111" opacity=".7"/><path d="M136 58l5 3-5 3z" fill="#fff"/>
  <rect x="0" y="106" width="227" height="20" fill="#111" opacity=".75"/>
  <path d="M26 112l5 3-5 3z" fill="#fff"/>
  <rect x="45" y="114" width="140" height="3" fill="#555"/><rect x="45" y="114" width="60" height="3" fill="#3a8fd0"/>
</svg>

<h2 style="left:96px;top:717px">Upcoming Events</h2>
<h2 style="left:338px;top:719px">Featured Articles</h2>
<h2 style="left:580px;top:719px">Events Gallery</h2>
<svg class="abs" style="left:768px;top:726px" width="32" height="16" viewBox="0 0 32 16"><path d="M9 2L3 8l6 6M21 2l6 6-6 6" fill="none" stroke="#555" stroke-width="2.4"/></svg>

<!-- Upcoming Events -->
<div class="photo" style="left:96px;top:771px;width:80px;height:56px;background:linear-gradient(180deg,#2a1a30,#b03048)" role="img" aria-label="Event hall with starry ceiling"></div>
<div class="item-title short" style="left:184px;top:769px">Design Your Flight-2013</div>
<div class="item-desc" style="left:184px;top:790px">An International Style of Competition now in INDIA. First time in INDIA</div>
<div class="btn" style="left:257px;top:845px;width:66px">View More</div>

<div class="photo" style="left:97px;top:875px;width:80px;height:57px;background:linear-gradient(180deg,#3a4aa8,#c8a0d8 55%,#402a60)" role="img" aria-label="Decorated wedding hall in purple light"></div>
<div class="item-title" style="left:184px;top:873px">perspiciatis unde omnis</div>
<div class="item-title short" style="left:184px;top:888px">iste natus error</div>
<div class="item-desc" style="left:184px;top:910px">An International Style of Competition now in INDIA. First time in INDIA.</div>
<div class="btn" style="left:257px;top:947px;width:66px">View More</div>

<div class="photo" style="left:96px;top:983px;width:80px;height:57px;background:linear-gradient(180deg,#202a6a,#7a2a5a 60%,#201028)" role="img" aria-label="Banquet tables under blue and red lights"></div>
<div class="item-title" style="left:184px;top:979px">accusamus et iusto odio</div>
<div class="item-title short" style="left:184px;top:994px">dignissimos ducimus</div>
<div class="item-desc" style="left:184px;top:1016px">An International Style of Competition now in INDIA. First time in INDIA</div>
<div class="btn" style="left:257px;top:1062px;width:66px">View More</div>

<!-- Featured Articles -->
<div class="photo" style="left:339px;top:771px;width:80px;height:56px;background:radial-gradient(circle at 30% 25%,#f0b040,#9a4a14 45%,#1a0c06)" role="img" aria-label="Concert crowd under stage lights"></div>
<div class="item-title" style="left:427px;top:769px">denounce with righteous</div>
<div class="item-title short" style="left:427px;top:784px">indignation</div>
<div class="item-desc" style="left:427px;top:805px">An International Style of Competition now in INDIA. First time in INDIA.</div>
<div class="btn" style="left:498px;top:845px;width:66px">View More</div>

<div class="photo" style="left:340px;top:875px;width:79px;height:57px;background:linear-gradient(180deg,#4a1a10,#b0402a 55%,#2a0e08)" role="img" aria-label="Reception room with round dining tables"></div>
<div class="item-title" style="left:427px;top:873px">Temporibus autem</div>
<div class="item-title short" style="left:427px;top:888px">quibusdam et aut officiis</div>
<div class="item-desc" style="left:427px;top:910px">An International Style of Competition now in INDIA. First</div>
<div class="btn" style="left:498px;top:947px;width:66px">View More</div>

<div class="photo" style="left:339px;top:983px;width:80px;height:57px;background:linear-gradient(180deg,#d84a5a,#a82030 60%,#3a1010)" role="img" aria-label="Hall with red draped chairs"></div>
<div class="item-title" style="left:427px;top:979px">Nam libero tempore,</div>
<div class="item-title short" style="left:427px;top:997px">cum soluta nobis</div>
<div class="item-desc" style="left:427px;top:1019px">An International Style of Competition now in INDIA. First time in INDIA</div>
<div class="btn" style="left:498px;top:1062px;width:66px">View More</div>

<!-- Events Gallery -->
<div class="photo" style="left:587px;top:771px;width:211px;height:150px;background:radial-gradient(circle at 50% 40%,#9ad0ff,#2a6ac8 40%,#0a1a3a 90%)" role="img" aria-label="Arena with blue stage lighting"></div>
<div class="photo" style="left:587px;top:944px;width:64px;height:46px;background:linear-gradient(#3a3a30,#8a8a70)" role="img" aria-label="Dining tables outdoors"></div>
<div class="photo" style="left:661px;top:944px;width:64px;height:46px;background:linear-gradient(#6a2a50,#c8b0d0)" role="img" aria-label="Stage with light beams"></div>
<div class="photo" style="left:735px;top:944px;width:64px;height:46px;background:linear-gradient(#2a3aa8,#1a1030)" role="img" aria-label="Performer on lit stage"></div>
<div class="photo" style="left:587px;top:999px;width:64px;height:46px;background:linear-gradient(#4a3aa0,#b05a8a)" role="img" aria-label="Banquet in purple light"></div>
<div class="photo" style="left:661px;top:999px;width:64px;height:46px;background:linear-gradient(#5aa8e8,#10306a)" role="img" aria-label="Blue lit concert"></div>
<div class="photo" style="left:735px;top:999px;width:64px;height:46px;background:linear-gradient(#a82a20,#2a0a08)" role="img" aria-label="Red lit banquet hall"></div>
<div class="btn" style="left:710px;top:1062px;width:89px">More Videos</div>

<footer class="site-footer abs">
  <div class="footer-links">About Us<span>|</span>Convention &amp; Meeting Services<span>|</span>Social Events<span>|</span>Small Business<span>|</span>Testimonial</div>
  <div class="copyright">Copyright ©2013 Marigold Gathering Occasions &nbsp;- All rights reserved</div>
</footer>
</body>
</html>
```